Luxury Shea butter and Argan oil moisturiser label

We are a company selling organic skin care products, aimed at the luxury market, our main customers being women. We are looking for a simplistic, minimal design, yet high quality, with a seriousness about it. Colour is very important for this label and we will provide examples of what we're looking for.
Our company logo will be at the centre of the label and will take centre stage. All lettering will be PALATINO capital font, gold lettering.
It is a round, circular lable, 57mm diameter.

Updates
The colour idea/them im looking for is very similar to the Marlo video ''Velvet Static''. Or better yet, the artwork of Owen Castile, who is said to have had a strong influence on the video.check out the video on youtube and then you will understand the colours im interested in. Added Friday, January 29, 2016
Industry/Entity Type
It Company
Logo Text
UNREFINED SHEA BUTTER WITH ARGAN OIL. 100 ml. 3.5 oz
Look and feel
Each slider illustrates characteristics of the customer's brand and the style your logo design should communicate.

```html
<!DOCTYPE html>
<html lang="en">
<head>
<meta charset="utf-8">
<title>Unrefined Shea Butter with Argan Oil – Label</title>
<link rel="stylesheet" href="https://fonts.googleapis.com/css2?family=EB+Garamond:wght@500;600&display=swap">
<style>
  :root {
    --label-bg: #ffffff;
    --gold: #c4a265;
  }
  html, body {
    margin: 0;
    padding: 0;
    width: 1200px;
    height: 999px;
    overflow: hidden;
    background: var(--label-bg);
  }
  .label {
    display: block;
    width: 1200px;
    height: 999px;
  }
  .ring-title text {
    font-family: "EB Garamond", "Palatino Linotype", Palatino, serif;
    font-weight: 600;
    font-size: 50px;
    fill: var(--gold);
    text-anchor: middle;
  }
  .ring-volume {
    font-family: "EB Garamond", "Palatino Linotype", Palatino, serif;
    font-weight: 600;
    font-size: 46px;
    letter-spacing: 4px;
    fill: var(--gold);
  }
  .ring-dot {
    fill: var(--gold);
  }
</style>
</head>
<body>
<svg class="label" viewBox="0 0 1200 999" xmlns="http://www.w3.org/2000/svg" role="img" aria-label="Unrefined Shea Butter with Argan Oil, 100 ml, 3.5 oz">
  <defs>
    <path id="volume-arc" d="M 288 498 A 312 312 0 0 0 912 498" fill="none"/>
  </defs>

  <g class="ring-title" aria-hidden="true">
    <text x="600" y="228" transform="rotate(-134 600 498)">U</text>
    <text x="600" y="228" transform="rotate(-124.76 600 498)">N</text>
    <text x="600" y="228" transform="rotate(-115.91 600 498)">R</text>
    <text x="600" y="228" transform="rotate(-107.89 600 498)">E</text>
    <text x="600" y="228" transform="rotate(-100.36 600 498)">F</text>
    <text x="600" y="228" transform="rotate(-94.33 600 498)">I</text>
    <text x="600" y="228" transform="rotate(-87.25 600 498)">N</text>
    <text x="600" y="228" transform="rotate(-78.67 600 498)">E</text>
    <text x="600" y="228" transform="rotate(-70.15 600 498)">D</text>

    <text x="600" y="228" transform="rotate(-57.76 600 498)">S</text>
    <text x="600" y="228" transform="rotate(-49.68 600 498)">H</text>
    <text x="600" y="228" transform="rotate(-41.05 600 498)">E</text>
    <text x="600" y="228" transform="rotate(-32.87 600 498)">A</text>

    <text x="600" y="228" transform="rotate(-20.25 600 498)">B</text>
    <text x="600" y="228" transform="rotate(-11.84 600 498)">U</text>
    <text x="600" y="228" transform="rotate(-3.43 600 498)">T</text>
    <text x="600" y="228" transform="rotate(4.31 600 498)">T</text>
    <text x="600" y="228" transform="rotate(12.06 600 498)">E</text>
    <text x="600" y="228" transform="rotate(20.08 600 498)">R</text>

    <text x="600" y="228" transform="rotate(34.46 600 498)">W</text>
    <text x="600" y="228" transform="rotate(42.65 600 498)">I</text>
    <text x="600" y="228" transform="rotate(48.9 600 498)">T</text>
    <text x="600" y="228" transform="rotate(57.53 600 498)">H</text>

    <text x="600" y="228" transform="rotate(71.03 600 498)">A</text>
    <text x="600" y="228" transform="rotate(79.5 600 498)">R</text>
    <text x="600" y="228" transform="rotate(88.19 600 498)">G</text>
    <text x="600" y="228" transform="rotate(97.04 600 498)">A</text>
    <text x="600" y="228" transform="rotate(106.06 600 498)">N</text>

    <text x="600" y="228" transform="rotate(119.89 600 498)">O</text>
    <text x="600" y="228" transform="rotate(126.97 600 498)">I</text>
    <text x="600" y="228" transform="rotate(133 600 498)">L</text>
  </g>

  <circle class="ring-dot" cx="426" cy="732" r="10"/>
  <circle class="ring-dot" cx="776" cy="732" r="10"/>

  <text class="ring-volume">
    <textPath href="#volume-arc" startOffset="50%" text-anchor="middle">100 ml. 3.5 oz</textPath>
  </text>
</svg>
</body>
</html>
```